RB Promotions a premium promotional agency needs design of business cards

I'm looking for a premium classy business card - possibly the Logo (the two backward R's) to be raised. Black and white for colour scheme would be preferable. I have attached my initial idea but open to your suggestions. We are a promotional agency who promote high profile brands. Thank you.

Contact Information for Business Card

MARLA WHITCOMBE
+64 21 555 0193
Marla@RBpromoagency.net
www.RBpromoagency.net

Colors
000000
ffffff

```html
<!DOCTYPE html>
<html lang="en">
<head>
<meta charset="utf-8">
<title>RB Promotions – Business Cards</title>
<link rel="stylesheet" href="https://fonts.googleapis.com/css2?family=Cormorant+Garamond:wght@500;600&display=swap">
<style>
  :root {
    --stage: #262626;
    --card: #0a0a0a;
    --card-sheen: #1c1c1c;
    --ink: #ffffff;
    --ink-soft: #e6e6e6;
    --rule: rgba(255, 255, 255, 0.85);
  }
  * { box-sizing: border-box; margin: 0; padding: 0; }
  html, body {
    width: 1200px;
    height: 660px;
    overflow: hidden;
    background: var(--stage);
  }
  .canvas {
    width: 1200px;
    height: 660px;
    display: flex;
    align-items: center;
    justify-content: center;
    gap: 48px;
    font-family: "Cormorant Garamond", Georgia, serif;
    color: var(--ink);
  }
  .card {
    position: relative;
    width: 520px;
    height: 297px;
    background: radial-gradient(ellipse at 55% 30%, var(--card-sheen) 0%, var(--card) 70%);
    box-shadow: 0 10px 30px rgba(0, 0, 0, 0.5);
  }
  .card__frame {
    position: absolute;
    inset: 14px;
    border: 1px solid var(--rule);
  }
  .card--front {
    display: flex;
    align-items: center;
    justify-content: center;
  }
  .brand-name {
    position: relative;
    font-size: 46px;
    font-weight: 500;
    letter-spacing: 0.5px;
    color: var(--ink);
  }
  .card--back {
    display: flex;
    flex-direction: column;
    align-items: center;
    justify-content: center;
    text-align: center;
  }
  .card--back .brand-name {
    font-size: 22px;
    letter-spacing: 1px;
    margin-bottom: 14px;
  }
  .person-name {
    position: relative;
    font-size: 28px;
    font-weight: 500;
    letter-spacing: 7px;
    margin-bottom: 26px;
  }
  .contact {
    position: relative;
    font-size: 13px;
    font-weight: 500;
    color: var(--ink-soft);
    line-height: 1.5;
    letter-spacing: 0.3px;
  }
  .contact__row span + span { margin-left: 18px; }
</style>
</head>
<body>
  <main class="canvas">
    <section class="card card--front">
      <div class="card__frame"></div>
      <div class="brand-name">RB Promotions</div>
    </section>

    <section class="card card--back">
      <div class="card__frame"></div>
      <div class="brand-name">RB Promotions</div>
      <h1 class="person-name">MARLA WHITCOMBE</h1>
      <div class="contact">
        <p class="contact__row"><span>T: +64 21 555 0193</span><span>E: Marla@RBpromoagency.net</span></p>
        <p class="contact__row">W: www.RBpromoagency.net</p>
      </div>
    </section>
  </main>
</body>
</html>
```